Banner Ad Design Project

We need banner ads for a website size:
728 x 90
160 x 90

Look at our website and you can see the color green we use throughout our advertising.

We have copy for 4 ads that should be interchangable

1. EHR me ASAP. Sign up in minutes.
2. Connect. Collaborate. Immediate. Sign up in minutes.
3. No software. No downloads. No charge.
4. EMR + HIE + PMR = FREE

Physicians

Software

```html
<!DOCTYPE html>
<html lang="en">
<head>
<meta charset="utf-8">
<title>Cellora Systems – Banner Set</title>
<link href="https://fonts.googleapis.com/css2?family=Open+Sans:wght@400;600&display=swap" rel="stylesheet">
<style>
  :root {
    --backdrop: #8c857c;
    --frame: #e4eed9;
    --panel: #ffffff;
    --brand-green: #7dc242;
    --ink-grey: #5b5b5b;
    --divider: #9fcf78;
    --button-top: #8a9678;
    --button-bottom: #5f6b52;
    --button-text: #ffffff;
  }
  * { margin: 0; padding: 0; box-sizing: border-box; }
  html, body {
    width: 1200px; height: 900px; overflow: hidden;
    background: var(--backdrop);
    font-family: "Open Sans", Arial, sans-serif;
  }
  .banner-set { position: relative; width: 1200px; height: 900px; }
  .banner {
    position: absolute; left: 45px; width: 1092px; height: 135px;
    background: var(--frame); padding: 6px;
  }
  .banner--ehr { top: 144px; }
  .banner--connect { top: 300px; }
  .banner--free-list { top: 455px; }
  .banner--equation { top: 610px; }
  .banner__panel {
    position: relative; width: 100%; height: 100%; background: var(--panel);
  }
  .brand {
    position: absolute; left: 27px; top: 34px;
    display: flex; align-items: center; gap: 10px;
    color: var(--brand-green); font-weight: 400; font-size: 27px; line-height: 1;
  }
  .brand__dot {
    width: 22px; height: 22px; border-radius: 50%; background: var(--brand-green);
  }
  .brand__name { display: flex; flex-direction: column; line-height: 1.05; }
  .divider {
    position: absolute; left: 234px; top: 18px; width: 2px; height: 87px;
    background: var(--divider);
  }
  .copy { position: absolute; left: 261px; font-weight: 600; line-height: 1.1; }
  .copy--ehr { top: 22px; }
  .copy__headline { color: var(--brand-green); font-size: 29px; }
  .copy__sub { color: var(--ink-grey); font-size: 33px; }
  .copy__tagline { color: var(--brand-green); font-size: 16px; word-spacing: 4px; margin-bottom: 4px; }
  .copy--connect { top: 26px; }
  .copy--list { top: 19px; left: 290px; font-size: 26px; line-height: 1.0; }
  .copy--list .is-green { color: var(--brand-green); }
  .copy--list .is-grey { color: var(--ink-grey); }
  .copy--equation { top: 42px; color: var(--brand-green); font-size: 25px; }
  .copy--equation .copy__free { color: var(--ink-grey); font-size: 33px; font-weight: 400; }
  .signup-button {
    position: absolute; left: 606px; top: 41px; width: 153px; height: 39px;
    border-radius: 3px;
    background: linear-gradient(var(--button-top), var(--button-bottom));
    color: var(--button-text); font-size: 13px; font-weight: 400;
    display: flex; align-items: center; justify-content: center;
  }
  .banner__visual { position: absolute; right: 0; top: 0; width: 305px; height: 100%; }
  .banner__visual--team {
    background: linear-gradient(90deg, #ffffff 0%, #e9eef5 25%, #9fb6d8 55%, #eef2f7 75%, #8fa6cf 100%);
  }
  .banner__visual--lab {
    background: linear-gradient(90deg, #ffffff 0%, #dde6ec 30%, #c47a6a 48%, #8aa7c9 65%, #6f90c9 85%, #eef2f6 100%);
  }
</style>
</head>
<body>
<main class="banner-set">

  <section class="banner banner--ehr">
    <div class="banner__panel">
      <div class="brand"><span class="brand__dot"></span><span class="brand__name"><span>Cellora</span><span>Systems</span></span></div>
      <div class="divider"></div>
      <div class="copy copy--ehr">
        <p class="copy__headline">EHR me ASAP</p>
        <p class="copy__sub">Sign up in minutes</p>
      </div>
      <div class="signup-button">Sign Up For Free</div>
      <div class="banner__visual banner__visual--team" role="img" aria-label="Photo of a team of physicians and nurses in white coats and scrubs"></div>
    </div>
  </section>

  <section class="banner banner--connect">
    <div class="banner__panel">
      <div class="brand"><span class="brand__dot"></span><span class="brand__name"><span>Cellora</span><span>Systems</span></span></div>
      <div class="divider"></div>
      <div class="copy copy--connect">
        <p class="copy__tagline">Connect Collaborate Coordinate Care</p>
        <p class="copy__sub">Sign up in minutes</p>
      </div>
      <div class="signup-button">Sign Up For Free</div>
      <div class="banner__visual banner__visual--team" role="img" aria-label="Photo of a team of physicians and nurses in white coats and scrubs"></div>
    </div>
  </section>

  <section class="banner banner--free-list">
    <div class="banner__panel">
      <div class="brand"><span class="brand__dot"></span><span class="brand__name"><span>Cellora</span><span>Systems</span></span></div>
      <div class="divider"></div>
      <div class="copy copy--list">
        <p class="is-green">No software</p>
        <p class="is-grey">No downloads</p>
        <p class="is-green">No charge</p>
      </div>
      <div class="signup-button">Sign Up For Free</div>
      <div class="banner__visual banner__visual--lab" role="img" aria-label="Photo of laboratory glassware: test tubes with coloured liquids in a rack and round flasks"></div>
    </div>
  </section>

  <section class="banner banner--equation">
    <div class="banner__panel">
      <div class="brand"><span class="brand__dot"></span><span class="brand__name"><span>Cellora</span><span>Systems</span></span></div>
      <div class="divider"></div>
      <div class="copy copy--equation">
        <p>EMR + HIE + PHR = <span class="copy__free">FREE</span></p>
      </div>
      <div class="signup-button">Sign Up For Free</div>
      <div class="banner__visual banner__visual--lab" role="img" aria-label="Photo of laboratory glassware: test tubes with coloured liquids in a rack and round flasks"></div>
    </div>
  </section>

</main>
</body>
</html>
```